Concept design for a tea business Labels

Hello, we are looking for concepts for our label/packaging for a tea business that has been in business now for over a year. We are a beachy, organic, "It's your moment. Enjoy it." type tea business. We have an online website (www.corvalbrewhouse.com.au) and sell at local markets around the Tarrowby Cove area.
We are looking to upgrade our label to look more professional, in a fun/beachy/chilled out style. (unlike the traditional tea labels).
We do loose leaf tea and iced tea consentrated syrups. We have a few different packages (please see website under "sizes and packaging" bottom left). We would like to experiement with various different size and shape of labels for different products, so would like a concept design for a label using our logo (see website front page bottom). There are no colour constraints.
We use the Quillan brand labels of the following sizes:
1. Pure Glass Rectangular Product Labels, Q4825, 100/Pack, 96 x 50.8 mm
2. Pure Glass Round Multi-purpose Labels, Q3907D, 240/Pack, 40 mm diameter
3.Pure Glass Square Product Labels, Q4861, 350/Pack, 35 x 35 mm
4. For bottles we use Grained Ivory Curved Labels, Q4839, 90/Pack, 57.2 x 77 mm
If you have any more questions, please don't hesitate to contact me
Updates
Hi All,
I am considering using a box like below for packing and doing a bit of a white/beachy feel to the packaging. Either using the rectangle or round circle labels. (circle labels from quillan 60mm diameter).

Reason: Hi All - Thank you so much for all your designs. While I have seen some really beautiful designs I am excited about, it seems there was a rush at the end with a number of new designs just submitted. I still haven't seen just one design I love for the label, so I would like the opportunity to work with some of the new designers to see if we can modify to suit the concept.
Would anyone like to try a concept label with a silhouette of one of the following wave/beach/teacup? I'm just exploring a different approach as I know it is difficult tying in the beach with tea - please think - chilled out beach hut with tea/iced tea, sunrise over ocean. I like the soft colour palette - beachy feel to it - ie. Pastels - blues, greens, whites, sandy, pinks, purples, greys - sunrises over ocean, maybe a white rustic wood feel - or any other icon from Tarrowby Cove - like the Norfolk Pine's along the beach - maybe in Silhouette.
Just some more ideas.
Thank you again for all your contributions!
Petra

```html
<!DOCTYPE html>
<html lang="en">
<head>
<meta charset="utf-8">
<title>Tarrowby Tea Company – Label Concept Tea #1</title>
<link rel="stylesheet" href="https://fonts.googleapis.com/css2?family=Open+Sans:wght@300;400;600;700&display=swap">
<style>
  :root {
    --stage-grey: #e3e4e6;
    --panel-white: #ffffff;
    --label-edge: #c9c9c9;
    --brand-brown: #a4642a;
    --band-green: #2f9a74;
    --band-green-light: #5cc39c;
    --band-highlight: #b9d8c9;
    --sun-gold: #e0ac24;
    --splash-yellow: #e3c51c;
    --leaf-tint: #d6ece4;
    --caption-ink: #231f20;
    --text-white: #ffffff;
  }
  html, body {
    margin: 0;
    padding: 0;
    overflow: hidden;
    background: var(--stage-grey);
  }
  .canvas {
    position: relative;
    width: 1200px;
    height: 1000px;
    background: var(--stage-grey);
    font-family: "Open Sans", Arial, sans-serif;
  }
  .presentation-panel {
    position: absolute;
    left: 45px;
    top: 55px;
    width: 1125px;
    height: 910px;
    background: var(--panel-white);
    border-radius: 28px;
    box-shadow: 0 0 18px 10px var(--panel-white);
  }
  .label-art {
    position: absolute;
    left: 0;
    top: 0;
  }
  .brand-name {
    font-family: "Open Sans", Arial, sans-serif;
    font-weight: 400;
    fill: var(--brand-brown);
  }
  .band-text {
    font-weight: 400;
    fill: var(--text-white);
    letter-spacing: 9px;
  }
  .tagline {
    font-weight: 300;
    fill: var(--text-white);
    letter-spacing: 4px;
  }
  .tagline-strong {
    font-weight: 700;
    fill: var(--text-white);
    letter-spacing: 6px;
  }
  .caption {
    position: absolute;
    left: 0;
    top: 842px;
    width: 1180px;
    text-align: center;
    font-size: 46px;
    font-weight: 400;
    color: var(--caption-ink);
    margin: 0;
  }
</style>
</head>
<body>
<div class="canvas">
  <div class="presentation-panel"></div>

  <svg class="label-art" width="1200" height="1000" viewBox="0 0 1200 1000" xmlns="http://www.w3.org/2000/svg">
    <defs>
      <clipPath id="label-shape">
        <rect x="97" y="99" width="966" height="722" rx="72" ry="72"/>
      </clipPath>
      <linearGradient id="band-sheen" x1="97" y1="0" x2="1063" y2="0" gradientUnits="userSpaceOnUse">
        <stop offset="0" stop-color="var(--band-green-light)"/>
        <stop offset="0.2" stop-color="var(--band-green)"/>
        <stop offset="0.46" stop-color="var(--band-highlight)"/>
        <stop offset="0.6" stop-color="var(--band-green)"/>
        <stop offset="0.78" stop-color="var(--band-green)"/>
        <stop offset="1" stop-color="var(--band-green-light)"/>
      </linearGradient>
      <linearGradient id="leaf-strip-fade" x1="0" y1="0" x2="0" y2="1">
        <stop offset="0" stop-color="var(--leaf-tint)" stop-opacity="0.55"/>
        <stop offset="1" stop-color="var(--leaf-tint)" stop-opacity="0.35"/>
      </linearGradient>
      <radialGradient id="splash-glow" cx="0.35" cy="0.5" r="0.7">
        <stop offset="0" stop-color="var(--splash-yellow)"/>
        <stop offset="1" stop-color="var(--sun-gold)"/>
      </radialGradient>
    </defs>

    <!-- tea splash spilling past the label edge -->
    <path role="img" aria-label="Yellow tea splash illustration"
          d="M1010 690 C1050 660 1090 660 1120 690 C1150 715 1160 760 1140 790 C1120 820 1070 830 1030 815 C1010 805 1000 760 1010 690 Z"
          fill="url(#splash-glow)" stroke="var(--label-edge)" stroke-width="2"/>

    <g clip-path="url(#label-shape)">
      <rect class="label-ground" x="97" y="99" width="966" height="722" fill="var(--panel-white)"/>
      <!-- gold lower field -->
      <polygon class="gold-field" points="97,562 1063,450 1063,821 97,821" fill="var(--sun-gold)"/>
      <!-- green diagonal ribbon -->
      <polygon class="ribbon" points="97,522 1063,388 1063,450 97,562" fill="url(#band-sheen)"/>
      <!-- vertical leaf pattern strip -->
      <rect role="img" aria-label="Faint repeating tea leaf pattern strip"
            x="245" y="99" width="255" height="722" fill="url(#leaf-strip-fade)"/>
    </g>

    <rect class="label-outline" x="97" y="99" width="966" height="722" rx="72" ry="72"
          fill="none" stroke="var(--label-edge)" stroke-width="3"/>

    <!-- brand name -->
    <circle class="brand-dot" cx="470" cy="180" r="30" fill="var(--brand-brown)"/>
    <text class="brand-name" x="165" y="345" font-size="96">Tarrowby</text>
    <text class="brand-name" x="447" y="378" font-size="28" letter-spacing="6">Tea Company</text>

    <!-- ribbon wording -->
    <text class="band-text" font-size="30" transform="translate(200 542) rotate(-7.9)">Organic Tea</text>

    <!-- tagline block -->
    <circle class="tagline-mark" cx="818" cy="597" r="52" fill="var(--text-white)"/>
    <text class="tagline" x="820" y="685" font-size="38" text-anchor="middle">It's your moment.</text>
    <text class="tagline-strong" x="826" y="745" font-size="34" text-anchor="middle">Enjoy it.</text>
  </svg>

  <p class="caption">Proposed Revised Design Tea #1</p>
</div>
</body>
</html>
```